Card design for orthopaedic surgeons working as The Brindlewood Orthopaedic Centre

Business cards, letterhead

Colors

Designer to choose colors to be used in the design.

Requirements
Must have
• Late addition.
• Cards letterhead must have logos of
• Corvane Federated Institute of Surgeons
• Meridale Orthopaedic Society
Nice to have
• Back of card to have space for appointment time to be added by hand and some blank space for writing incidental other notes.

```html
<!DOCTYPE html>
<html lang="en">
<head>
<meta charset="utf-8">
<title>The Brindlewood Orthopaedic Centre — Business Card</title>
<link href="https://fonts.googleapis.com/css2?family=Roboto:wght@400;500;700&display=swap" rel="stylesheet">
<style>
  :root {
    --canvas-bg: #808080;
    --card-white: #ffffff;
    --brand-blue: #3b92d2;
    --accent-blue: #4a9fdc;
    --ink: #1c1c1c;
  }
  * { box-sizing: border-box; margin: 0; padding: 0; }
  html, body {
    width: 1200px; height: 1020px; overflow: hidden;
    background: var(--canvas-bg);
    font-family: "Roboto", Arial, sans-serif;
  }
  .canvas { position: relative; width: 1200px; height: 1020px; }
  .card {
    position: absolute; width: 656px; height: 376px;
    border-radius: 20px; overflow: hidden;
  }
  .card--front { left: 272px; top: 88px; background: var(--card-white); }
  .card--back { left: 271px; top: 514px; background: var(--brand-blue); }

  .brand-name {
    position: absolute; font-weight: 400; white-space: nowrap; letter-spacing: -0.2px;
  }
  .card--front .brand-name {
    right: 22px; top: 116px; font-size: 15px; color: var(--accent-blue);
  }
  .card--back .brand-name {
    left: 0; right: 0; top: 186px; text-align: center;
    font-size: 27px; color: var(--card-white);
  }

  .holder { position: absolute; left: 22px; top: 110px; color: var(--ink); }
  .holder__name {
    font-size: 28px; font-weight: 700; color: var(--accent-blue);
    letter-spacing: 0.5px; line-height: 1;
  }
  .holder__role { font-size: 18px; margin-top: 5px; }

  .address { position: absolute; left: 24px; top: 196px; font-size: 17.5px; line-height: 23px; color: var(--ink); }

  .contacts { position: absolute; left: 24px; top: 272px; list-style: none; font-size: 17.5px; color: var(--ink); }
  .contacts li { display: flex; align-items: center; height: 25.5px; }
  .contacts svg { width: 13px; height: 13px; margin-right: 9px; fill: var(--accent-blue); }
</style>
</head>
<body>
<div class="canvas">
  <section class="card card--front">
    <div class="brand-name">The Brindlewood Orthopaedic Centre</div>
    <div class="holder">
      <div class="holder__name">ANSEL VARROW</div>
      <div class="holder__role">Owner</div>
    </div>
    <div class="address">418, Larkfield Avenue<br>Brookvale NY 11842</div>
    <ul class="contacts">
      <li>
        <svg viewBox="0 0 16 16" aria-hidden="true"><path d="M3.5 1.5l2.5 0 1.2 3.2-1.7 1.2c.8 1.8 2.2 3.2 4 4l1.2-1.7 3.2 1.2v2.5c0 .8-.7 1.5-1.5 1.5C6.6 13.4 2.6 9.4 2 3c0-.8.7-1.5 1.5-1.5z"/></svg>
        (555) 384-2716
      </li>
      <li>
        <svg viewBox="0 0 16 16" aria-hidden="true"><path d="M1 3h14v10H1z M1.8 3.6L8 8.6l6.2-5" fill="none" stroke="#4a9fdc" stroke-width="1.6"/><rect x="1" y="3" width="14" height="10" /></svg>
        ansel@yourmail.com
      </li>
      <li>
        <svg viewBox="0 0 16 16" aria-hidden="true"><circle cx="8" cy="8" r="7"/><path d="M4 5c1.5 0 2 1 3 1s.5 2-1 2.5S5 11 6 12.5M10 3c-.5 1.5.5 2 1.5 2.5S13 8 11.5 9" fill="none" stroke="#fff" stroke-width="1.1"/></svg>
        www.brindlewoodoc.com
      </li>
    </ul>
  </section>

  <section class="card card--back">
    <div class="brand-name">The Brindlewood Orthopaedic Centre</div>
  </section>
</div>
</body>
</html>
```